Trifold flyer for our dental clinic (the Bright Harbor Clinic)

The goal of this project is to design a trifold flyer for our dental clinic (the Bright Harbor Clinic). The winning design is expected to be creative, artistic and coherent with our logo.
Updates

Designs look the same

Target Market(s)

Young generation with dental need.

Industry/Entity Type

Dental Clinic

Font styles to use
Sans Serif

Colors
0355a3
85acd3
85cae6
0592cd
00a990
86cfc6
cedeed
cee9f5
cfeae6

Requirements
Must have
• See the attached sketch for content arrangement.

```html
<!DOCTYPE html>
<html lang="en">
<head>
<meta charset="utf-8">
<title>Bright Harbor Clinic – Trifold Front Panel</title>
<link rel="stylesheet" href="https://fonts.googleapis.com/css2?family=Oswald:wght@500;700&family=Open+Sans:wght@400;600&display=swap">
<style>
  :root {
    --bg: #e3e4e6;
    --paper: #ffffff;
    --ink: #333538;
    --blue: #1e9ad6;
    --blue-deep: #0592cd;
    --blue-light: #85cae6;
    --blue-pale: #cee9f5;
    --charcoal: #2b2d30;
    --photo-light: #f3f0c8;
    --photo-mid: #b9d77a;
    --photo-deep: #6f9c3c;
  }
  * { margin: 0; padding: 0; box-sizing: border-box; }
  html, body { width: 1200px; height: 900px; overflow: hidden; background: var(--bg); }
  body { position: relative; font-family: "Open Sans", Arial, sans-serif; }

  .flyer-panel {
    position: absolute; left: 410px; top: 30px;
    width: 380px; height: 840px;
    background: var(--paper);
    box-shadow: 0 6px 24px rgba(0,0,0,.12);
    overflow: hidden;
  }
  .panel-art { position: absolute; inset: 0; }

  .call-line {
    position: absolute; left: 28px; top: 28px;
    font-family: "Oswald", Arial, sans-serif; font-weight: 500;
    font-size: 24px; color: var(--ink); letter-spacing: .2px;
  }
  .phone-number {
    position: absolute; left: 26px; top: 56px;
    font-family: "Oswald", Arial, sans-serif; font-weight: 700;
    font-size: 62px; line-height: 1; color: var(--blue);
  }

  .clinic-name {
    position: absolute; left: 0; right: 0; top: 236px;
    display: flex; align-items: center; justify-content: center; gap: 10px;
    font-family: "Open Sans", Arial, sans-serif; font-weight: 600;
    font-size: 17px; letter-spacing: .6px; color: var(--blue);
  }
  .clinic-name .mark { width: 16px; height: 16px; background: var(--blue); }

  .offer-badge {
    position: absolute; left: 46px; top: 572px;
    width: 128px; height: 128px; border-radius: 50%;
    background: var(--blue-deep);
    border: 5px solid var(--paper);
    box-shadow: 0 0 0 4px var(--charcoal);
    display: flex; flex-direction: column; align-items: center; justify-content: center;
    transform: rotate(-22deg);
    font-family: "Oswald", Arial, sans-serif; font-weight: 700; color: var(--paper);
    line-height: .95;
  }
  .offer-badge .small { font-size: 28px; }
  .offer-badge .large { font-size: 38px; letter-spacing: 1px; }

  .offer-points {
    position: absolute; left: 26px; top: 722px; right: 12px;
    list-style: none; font-size: 10px; color: var(--ink); line-height: 2;
  }
  .offer-points li { position: relative; padding-left: 16px; white-space: nowrap; }
  .offer-points li::before {
    content: ""; position: absolute; left: 0; top: 6px;
    width: 8px; height: 8px; border-radius: 50%; background: var(--blue);
  }
</style>
</head>
<body>
  <section class="flyer-panel">
    <svg class="panel-art" width="380" height="840" viewBox="0 0 380 840">
      <defs>
        <linearGradient id="familyPhotoTone" x1="0" y1="0" x2="1" y2="1">
          <stop offset="0" stop-color="#f3f0c8"/>
          <stop offset=".5" stop-color="#b9d77a"/>
          <stop offset="1" stop-color="#6f9c3c"/>
        </linearGradient>
      </defs>
      <path d="M0 215 C120 165 250 150 380 175 L380 195 C250 172 120 185 0 235 Z" fill="#cee9f5"/>
      <path d="M0 205 C120 150 250 138 380 160 L380 170 C250 150 120 165 0 218 Z" fill="#0592cd"/>
      <path d="M340 300 C395 400 395 560 300 680 L318 690 C410 560 410 400 358 300 Z" fill="#2b2d30"/>
      <path d="M324 300 C375 400 375 550 290 668 L300 676 C388 550 388 400 336 300 Z" fill="#1e9ad6"/>
      <path role="img" aria-label="Photo of a smiling family lying together in a sunny green park"
            d="M0 300 C110 275 230 270 318 290 C370 400 365 545 280 662 C180 700 80 690 0 670 Z"
            fill="url(#familyPhotoTone)"/>
      <path d="M0 672 C80 694 180 704 282 668 L276 680 C180 716 80 706 0 686 Z" fill="#1e9ad6"/>
    </svg>

    <p class="call-line">call us for more information</p>
    <p class="phone-number">555.204.7318</p>

    <div class="clinic-name"><span class="mark"></span>BRIGHT HARBOR CLINIC</div>

    <div class="offer-badge">
      <span class="small">special</span>
      <span class="large">OFFER</span>
    </div>

    <ul class="offer-points">
      <li>Lorem ipsum dolor sit amet, consectetur adipiscing elit.</li>
      <li>Aenean vel sem suscipit odio molestie iaculis nec et mauris.</li>
      <li>Fusce sed nibh non mauris mollis feugiat.</li>
      <li>Pellentesque quis mauris vitae enim scelerisque placerat.</li>
    </ul>
  </section>
</body>
</html>
```